Business Cards

The name of our firm is "Tallpine Insurance adjusters"
We separate ourselves from all other public adjusters because most of us worked for the insurance companies so we understand their games.
As Insurance adjusters we represent the Insured, not the insurance companies. Our # 1 priority is to handle the entire claim process as seamless as possible on behalf of the homeowner/business owner so they don't have to deal with the hassles and headaches. Just as the logo your team designed, I want the cards to stand out from everyone elses. I also want the cards to help better understand our services and Value on hiring us and value that we can offer.
I uploaded the logo whenever I created the project. I don't see an option on re uploading the logo anywhere. Any advise??

```html
<!DOCTYPE html>
<html lang="en">
<head>
<meta charset="UTF-8">
<title>Tallpine Insurance Adjusters – Business Cards</title>
<link href="https://fonts.googleapis.com/css2?family=Montserrat:wght@600;700&family=Open+Sans:wght@400;600&display=swap" rel="stylesheet">
<style>
  :root {
    --page-bg: #e4e5e7;
    --brand-blue: #1472ad;
    --deep-blue: #0a4a78;
    --back-top: #1677ac;
    --back-bottom: #0a4e7d;
    --back-mark: #0c5283;
    --ink: #222428;
    --rule: #3a3c40;
    --card-white: #ffffff;
  }
  * { box-sizing: border-box; margin: 0; padding: 0; }
  html, body {
    width: 1200px; height: 900px; overflow: hidden;
    background: var(--page-bg);
  }
  .canvas {
    width: 1200px; height: 900px;
    display: flex; flex-direction: column; align-items: center; justify-content: center;
    gap: 56px;
  }
  .card {
    position: relative;
    width: 660px; height: 377px;
    border-radius: 26px;
    overflow: hidden;
    flex: none;
  }

  /* Back side */
  .card-back {
    background: linear-gradient(180deg, var(--back-top), var(--back-bottom));
    display: flex; align-items: center; justify-content: center;
  }
  .back-wordmark {
    display: flex; align-items: center; gap: 18px;
    font-family: "Montserrat", sans-serif; font-weight: 700;
    color: var(--back-mark);
    font-size: 36px; letter-spacing: 1px; text-transform: uppercase;
    line-height: 1.15;
  }
  .back-wordmark .mark-dot {
    flex: none;
    width: 40px; height: 40px; border-radius: 50%;
    background: var(--back-mark);
  }
  .back-wordmark .mark-name { white-space: nowrap; }

  /* Front side */
  .card-front { background: var(--card-white); }
  .front-wordmark {
    position: absolute; left: 44px; top: 56px;
    width: 260px;
    font-family: "Montserrat", sans-serif; font-weight: 700;
    color: var(--brand-blue);
    font-size: 26px; line-height: 1.1; text-transform: uppercase;
  }
  .front-wordmark .mark-square {
    display: block; width: 34px; height: 34px;
    background: var(--brand-blue); margin-bottom: 10px;
  }
  .person {
    position: absolute; right: 44px; top: 142px;
    text-align: right;
  }
  .person-name {
    font-family: "Montserrat", sans-serif; font-weight: 700;
    color: var(--brand-blue);
    font-size: 27px; letter-spacing: 1px; line-height: 1.2;
  }
  .person-title {
    font-family: "Open Sans", sans-serif; font-weight: 400;
    color: var(--ink); font-size: 17px; margin-top: 2px;
  }
  .divider {
    position: absolute; left: 36px; right: 36px; top: 224px;
    height: 1px; background: var(--rule);
  }
  .contact-list {
    position: absolute; left: 48px; top: 242px;
    list-style: none;
    font-family: "Open Sans", sans-serif; color: var(--ink);
    font-size: 18px;
  }
  .contact-list li {
    display: flex; align-items: center; gap: 12px;
    height: 32px;
  }
  .contact-list svg { width: 16px; height: 16px; flex: none; }
</style>
</head>
<body>
<main class="canvas">
  <section class="card card-back" aria-label="Card back">
    <div class="back-wordmark">
      <span class="mark-dot"></span>
      <span class="mark-name">Tallpine<br>Insurance Adjusters</span>
    </div>
  </section>

  <section class="card card-front" aria-label="Card front">
    <div class="front-wordmark">
      <span class="mark-square"></span>
      Tallpine Insurance Adjusters
    </div>

    <div class="person">
      <p class="person-name">DANIEL REYES</p>
      <p class="person-title">Founder/CEO</p>
    </div>

    <div class="divider"></div>

    <ul class="contact-list">
      <li>
        <svg viewBox="0 0 16 16" aria-hidden="true"><path fill="#1472ad" d="M3.6 1.5l2.2 2.6-1.3 1.7c.9 2 2.6 3.7 4.6 4.6l1.7-1.3 2.6 2.2-1.3 2.2C7.1 13.3 2.7 8.9 1.4 2.8z"/></svg>
        <span>321-555-0148</span>
      </li>
      <li>
        <svg viewBox="0 0 16 16" aria-hidden="true"><rect x="1" y="3" width="14" height="10" fill="#1472ad"/><path d="M1 3l7 6 7-6" fill="none" stroke="#fff" stroke-width="1.4"/></svg>
        <span>daniel@tallpineinsadj.com</span>
      </li>
      <li>
        <svg viewBox="0 0 16 16" aria-hidden="true"><circle cx="8" cy="8" r="7" fill="#1472ad"/><path d="M1 8h14M8 1c-3 3-3 11 0 14M8 1c3 3 3 11 0 14" fill="none" stroke="#fff" stroke-width="1"/></svg>
        <span>www.tallpineinsadj.com</span>
      </li>
    </ul>
  </section>
</main>
</body>
</html>
```